Online-Marketing Material
wir sind sehr zufrieden mit allem. danke
Zielgruppe
Wir vertreiben auf unserer Plattform morvelhaus17.de diverse Produkte rund um das Thema Kaffee. Unsere Zielgruppe sind Kaffeeliebhaber von jung bis alt.
Aufgabenstellung
Für unsere neue Domain brulino.at benötigen wir diverse Grafiken / Banner für die verschiedenen Bereiche unseres Shops. Momentan gibt es eine Staging Site um sich einen Überblick zu verschaffen.
Auftrag hier ist ein Startseitenbanner in der Größe 3200x1240 unter Berücksichtigung der aktuellen Farben in unserem Shop, der Thematik Kaffee und mehr und dem dazugehörigen neuen bereits entworfenem Logo.
Info Testseite: http://www.brulino.at/_staging/ Login mit admin und velo#482
Gerne kann eigenes Bildmaterial geliefert werden

```html
<!DOCTYPE html>
<html lang="de">
<head>
<meta charset="utf-8">
<title>brulino.at – Startseite</title>
<link href="https://fonts.googleapis.com/css2?family=Poppins:wght@400;500;700&family=Kaushan+Script&display=swap" rel="stylesheet">
<style>
  :root {
    --brand-red: #a52a27;
    --brand-brown: #3b2a1f;
    --text-dark: #1d1d1d;
    --muted-grey: #8a8a8a;
    --line: #ececec;
    --white: #ffffff;
  }
  * { margin: 0; padding: 0; box-sizing: border-box; }
  html, body { width: 1200px; height: 645px; overflow: hidden; background: var(--white); font-family: "Poppins", sans-serif; color: var(--text-dark); }
  .page { position: relative; width: 1200px; height: 645px; }

  .promo-bar { position: absolute; top: 0; left: 0; width: 1200px; height: 22px; background: var(--brand-red); color: var(--white); font-size: 8.5px; line-height: 22px; text-align: center; letter-spacing: .1px; }

  .search { position: absolute; left: 100px; top: 65px; width: 218px; height: 20px; border: 1px solid #333; border-radius: 10px; display: flex; align-items: center; padding: 0 8px; font-size: 8.5px; color: var(--muted-grey); justify-content: space-between; }

  .brand { position: absolute; left: 500px; top: 94px; width: 200px; text-align: center; font-weight: 700; font-size: 23px; line-height: 30px; color: var(--brand-brown); letter-spacing: .2px; }

  .header-tools { position: absolute; right: 112px; top: 66px; display: flex; align-items: center; gap: 11px; }
  .header-tools svg { width: 18px; height: 18px; stroke: var(--text-dark); fill: none; stroke-width: 1.6; }
  .cart { position: relative; }
  .cart-badge { position: absolute; top: -5px; right: -7px; width: 11px; height: 11px; border-radius: 50%; background: var(--brand-red); color: var(--white); font-size: 7px; line-height: 11px; text-align: center; }
  .cart-total { font-size: 10px; margin-left: 2px; }
  .cart-total sup { font-size: 6.5px; }

  .main-nav { position: absolute; top: 134px; left: 0; width: 1200px; display: flex; justify-content: center; gap: 18px; font-size: 10.8px; font-weight: 500; text-transform: uppercase; }
  .divider { position: absolute; top: 168px; left: 100px; width: 1000px; height: 1px; background: var(--line); }

  .hero { position: absolute; left: 100px; top: 169px; width: 1011px; height: 391px; background: linear-gradient(180deg, #ffffff 0%, #ffffff 56%, #cbb79c 62%, #b89d7c 80%, #a58a6b 100%); overflow: hidden; }
  .hero-photo { position: absolute; left: 580px; top: 60px; width: 431px; height: 331px; background: radial-gradient(ellipse 48% 50% at 50% 58%, #f3efea 0%, #d7c2a6 35%, #8a5d3b 70%, rgba(138,93,59,0) 100%); }
  .hero-headline { position: absolute; left: 0; top: 0; width: 700px; height: 240px; font-family: "Kaushan Script", cursive; }
  .hero-headline .line-main { position: absolute; left: 8px; top: 8px; font-size: 150px; line-height: 170px; color: var(--brand-brown); white-space: nowrap; }
  .hero-headline .line-sub { position: absolute; left: 306px; top: 140px; font-size: 66px; line-height: 80px; color: var(--brand-red); white-space: nowrap; }
  .hero-badge { position: absolute; left: 861px; top: 241px; width: 135px; height: 135px; background: var(--white); display: flex; align-items: flex-end; justify-content: center; padding-bottom: 16px; font-weight: 700; font-size: 21px; color: var(--brand-brown); }

  .brand-carousel { position: absolute; top: 585px; left: 100px; width: 1000px; height: 38px; }
  .carousel-arrow { position: absolute; top: 0; width: 19px; height: 38px; border: 1px solid #333; display: flex; align-items: center; justify-content: center; }
  .carousel-arrow svg { width: 8px; height: 14px; stroke: #333; fill: none; stroke-width: 1.3; }
  .carousel-arrow.prev { left: 0; border-left: none; }
  .carousel-arrow.next { right: 0; border-right: none; }
  .brand-list { position: absolute; left: 40px; right: 40px; top: 0; height: 38px; display: flex; justify-content: space-between; align-items: center; }
  .brand-list span { width: 110px; text-align: center; font-size: 16px; font-weight: 500; color: var(--muted-grey); }
</style>
</head>
<body>
<div class="page">
  <div class="promo-bar">Frische Garantie - Beste Markenqualität - Lieferung in 1-3 Werktagen</div>

  <div class="search">
    <span>Suchbegriff eingeben...</span>
    <svg width="13" height="13" viewBox="0 0 16 16" fill="none" stroke="#111" stroke-width="1.8"><circle cx="6.5" cy="6.5" r="5"/><path d="M10.3 10.3 15 15"/></svg>
  </div>

  <div class="brand">brulino.at</div>

  <div class="header-tools">
    <svg viewBox="0 0 24 24"><path d="M12 20s-8-5-8-11a4.5 4.5 0 0 1 8-2.8A4.5 4.5 0 0 1 20 9c0 6-8 11-8 11z"/></svg>
    <svg viewBox="0 0 24 24"><circle cx="12" cy="8" r="4"/><path d="M4 21c0-4.4 3.6-7 8-7s8 2.6 8 7"/></svg>
    <div class="cart">
      <svg viewBox="0 0 24 24"><path d="M4 8h16v12H4z"/><path d="M9 8V6a3 3 0 0 1 6 0v2"/></svg>
      <span class="cart-badge">0</span>
    </div>
    <span class="cart-total">0,<sup>00*</sup></span>
  </div>

  <nav class="main-nav">
    <span>Kaffee &amp; Espresso</span>
    <span>Pure Tee - Feldmark</span>
    <span>Kaffeekapseln</span>
    <span>Kaffeepads</span>
    <span>Büro Kaffee Service</span>
    <span>Probierpakete</span>
    <span>Angebote &amp; Neu</span>
  </nav>
  <div class="divider"></div>

  <section class="hero">
    <div class="hero-photo" role="img" aria-label="Weiße Kaffeetasse und Jutesack mit Kaffeebohnen auf Holztisch"></div>
    <h1 class="hero-headline">
      <span class="line-main">Kaffee</span>
      <span class="line-sub">und mehr</span>
    </h1>
    <div class="hero-badge">brulino.at</div>
  </section>

  <div class="brand-carousel">
    <div class="carousel-arrow prev"><svg viewBox="0 0 8 14"><path d="M7 1 1 7l6 6"/></svg></div>
    <div class="brand-list">
      <span>Solvento</span>
      <span>Carvelli</span>
      <span>Orsello</span>
      <span>Torrano</span>
      <span>Dravino</span>
      <span>Lumesso</span>
    </div>
    <div class="carousel-arrow next"><svg viewBox="0 0 8 14"><path d="M1 1l6 6-6 6"/></svg></div>
  </div>
</div>
</body>
</html>
```